Business Card Design

Certified KFL Instructor. Self defense instruction. Ladies classes available. Semi automatic and revolver

Industry/Entity Type

Defense

```html
<!DOCTYPE html>
<html lang="en">
<head>
<meta charset="utf-8">
<title>Business Card – Dana Holloway</title>
<link href="https://fonts.googleapis.com/css2?family=Lato:wght@700;900&display=swap" rel="stylesheet">
<style>
  :root {
    --backdrop: #2e2e2e;
    --card: #f4f4f4;
    --card-edge: #e2e2e2;
    --ink: #111111;
  }
  html, body {
    margin: 0;
    padding: 0;
    width: 1200px;
    height: 1116px;
    overflow: hidden;
    background: var(--backdrop);
  }
  .stage {
    position: relative;
    width: 1200px;
    height: 1116px;
    display: flex;
    align-items: center;
    justify-content: center;
  }
  .business-card {
    position: relative;
    width: 900px;
    height: 514px;
    border-radius: 34px;
    background: linear-gradient(160deg, #ffffff 0%, var(--card) 55%, var(--card-edge) 100%);
    box-shadow: 0 18px 40px rgba(0, 0, 0, 0.45);
    font-family: "Lato", sans-serif;
    color: var(--ink);
  }
  .holder-name {
    position: absolute;
    right: 120px;
    top: 254px;
    margin: 0;
    font-size: 26px;
    font-weight: 900;
    letter-spacing: 0.5px;
  }
  .divider {
    position: absolute;
    left: 92px;
    right: 118px;
    top: 292px;
    height: 3px;
    background: var(--ink);
  }
  .contact-list {
    position: absolute;
    left: 92px;
    top: 326px;
    margin: 0;
    padding: 0;
    list-style: none;
  }
  .contact-item {
    display: flex;
    align-items: center;
    gap: 14px;
    font-size: 22px;
    font-weight: 700;
    height: 44px;
  }
  .contact-icon {
    width: 22px;
    height: 22px;
    fill: var(--ink);
    flex: none;
  }
</style>
</head>
<body>
<main class="stage">
  <article class="business-card">
    <h1 class="holder-name">DANA HOLLOWAY</h1>
    <div class="divider"></div>
    <ul class="contact-list">
      <li class="contact-item">
        <svg class="contact-icon" viewBox="0 0 24 24" aria-hidden="true">
          <path d="M3 8c0-2 4-4 9-4s9 2 9 4v2h-5V8.5c-1-.6-2.4-.9-4-.9s-3 .3-4 .9V10H3z"/>
          <path d="M6 12h12l2 8H4z M12 14a2.5 2.5 0 1 0 0 5a2.5 2.5 0 1 0 0-5z" fill-rule="evenodd"/>
        </svg>
        <span>555-318-2047</span>
      </li>
      <li class="contact-item">
        <svg class="contact-icon" viewBox="0 0 24 24" aria-hidden="true">
          <path d="M2 5h20v14H2z M4 7v.4l8 5.6 8-5.6V7z" fill-rule="evenodd"/>
        </svg>
        <span>hollowayd@mailbox.com</span>
      </li>
    </ul>
  </article>
</main>
</body>
</html>
```